We would like to have a poster designed for our new fitness program called " Golden Orchard Program ". It consists of 1 assessment by a registered physiotherapist and 5 closely monitored exercise sessions. the goal of the program is to develop a strong back to meed the daily demands and sport activities. Ideal program for the people who sit all day for work. Green is our theme color of the clinic. We are open for other colors as well.The poster design should communicate fitness and strength. One time cost of the program is $ 350 . We will see the patient once per week for 6 weeks.

Target Market(s)

People with sitting job and heavy labor job.
Athelets
Active individuals who wanna participate in yoga, running, fitness classes etc.

Industry/Entity Type

Fitness

Font styles to use
Serif

Requirements
Must have
• simplicity and strong message.
Nice to have
• pain free spine picture

```html
<!DOCTYPE html>
<html lang="en">
<head>
<meta charset="utf-8">
<title>Golden Orchard Program – Poster</title>
<link rel="stylesheet" href="https://fonts.googleapis.com/css2?family=Bebas+Neue&family=Oswald:wght@400;500&display=swap">
<style>
  :root {
    --green-light: #9cc236;
    --green-mid: #74a11d;
    --green-dark: #3f6a0c;
    --orange: #f3901c;
    --orange-deep: #d96a0a;
    --shadow-brown: #5a3408;
    --white: #ffffff;
    --ink: #141414;
    --link-green: #7fb321;
  }
  * { margin: 0; padding: 0; box-sizing: border-box; }
  html, body { width: 960px; height: 1200px; overflow: hidden; background: var(--white); }
  .poster {
    position: relative;
    width: 960px;
    height: 1200px;
    overflow: hidden;
    background: radial-gradient(ellipse at 50% 45%, var(--green-light) 0%, var(--green-mid) 55%, var(--green-dark) 100%);
    font-family: "Oswald", "Arial Narrow", sans-serif;
  }
  .athletes-photo {
    position: absolute;
    left: 48px; top: 400px;
    width: 864px; height: 520px;
    background:
      radial-gradient(ellipse at 25% 45%, rgba(243,144,28,0.45) 0%, rgba(243,144,28,0) 45%),
      radial-gradient(ellipse at 75% 40%, rgba(243,144,28,0.45) 0%, rgba(243,144,28,0) 45%),
      radial-gradient(ellipse at 50% 50%, rgba(200,220,120,0.25) 0%, rgba(200,220,120,0) 70%);
  }
  .title {
    position: absolute;
    left: 0; width: 100%;
    text-align: center;
    font-family: "Bebas Neue", "Oswald", sans-serif;
    color: var(--white);
    line-height: 1;
    text-shadow: 4px 4px 0 var(--orange), 7px 7px 0 var(--shadow-brown);
  }
  .title-top { top: 60px; font-size: 150px; letter-spacing: 2px; }
  .title-bottom { top: 196px; font-size: 218px; letter-spacing: 3px; }
  .price-frame { position: absolute; left: 366px; top: 420px; width: 232px; height: 330px; }
  .price {
    position: absolute;
    left: 386px; top: 452px;
    font-family: "Bebas Neue", "Oswald", sans-serif;
    color: var(--white);
    line-height: 1;
  }
  .price-amount { display: block; font-size: 118px; }
  .price-note { display: block; font-size: 66px; margin-top: 2px; }
  .price-label { display: block; font-size: 104px; margin-top: -4px; }
  .schedule {
    position: absolute;
    left: -4px; top: 837px;
    width: 369px; height: 102px;
    border: 3px solid var(--white);
    display: flex; align-items: center; justify-content: center;
    text-align: center;
    color: var(--white);
    font-weight: 500;
    font-size: 21px;
    line-height: 1.6;
    text-transform: uppercase;
  }
  .footer-wave { position: absolute; left: 0; top: 900px; width: 960px; height: 300px; }
  .brand {
    position: absolute;
    left: 660px; top: 958px;
    width: 220px;
    font-family: "Oswald", sans-serif;
    font-weight: 500;
    font-size: 36px;
    line-height: 1.05;
    color: var(--orange);
    text-align: center;
  }
  .contact {
    position: absolute;
    left: 0; width: 100%;
    text-align: center;
    color: var(--ink);
    font-size: 25px;
    line-height: 1;
  }
  .contact-address { top: 1100px; }
  .contact-lines { top: 1142px; }
  .contact-web { color: var(--link-green); }
  .contact-mail { color: var(--orange); }
</style>
</head>
<body>
<main class="poster">
  <div class="athletes-photo" role="img" aria-label="Two athletes training with dumbbells, toned in orange over the green background"></div>

  <h1>
    <span class="title title-top">Golden Orchard</span>
    <span class="title title-bottom">Program</span>
  </h1>

  <svg class="price-frame" viewBox="0 0 232 330" aria-hidden="true">
    <polyline points="4,58 4,4 58,4" fill="none" stroke="#ffffff" stroke-width="6"/>
    <polyline points="228,272 228,326 174,326" fill="none" stroke="#ffffff" stroke-width="6"/>
  </svg>
  <p class="price">
    <span class="price-amount">$350</span>
    <span class="price-note">One Time</span>
    <span class="price-label">Cost</span>
  </p>

  <p class="schedule">We will see the patient once<br>per week for 6 weeks</p>

  <svg class="footer-wave" viewBox="0 0 960 300" preserveAspectRatio="none" aria-hidden="true">
    <defs>
      <linearGradient id="stripe" x1="0" y1="0" x2="1" y2="0">
        <stop offset="0" stop-color="#f3901c" stop-opacity="0.2"/>
        <stop offset="0.5" stop-color="#f3901c"/>
        <stop offset="1" stop-color="#d96a0a"/>
      </linearGradient>
    </defs>
    <path d="M0,80 C260,10 560,150 960,40 L960,300 L0,300 Z" fill="url(#stripe)"/>
    <path d="M0,100 C260,30 560,170 960,62 L960,300 L0,300 Z" fill="#ffffff"/>
  </svg>

  <p class="brand">Stridewell<br>Physical Therapy</p>

  <p class="contact contact-address">2281-88 street NW Riverton. Alberta. T4K2R7.</p>
  <p class="contact contact-lines">Phone: 780 555 0147 <span class="contact-web">www.stridewellphysio.ca</span> <span class="contact-mail">stridewellphysio@mailbox.ca</span></p>
</main>
</body>
</html>
```